Business Card Design

We would like a business card that utilizes our current logo and keeps with the same feel - elegant and organic. Our farm isn't about mass production, it's about excellence, education, beautiful events and flowers - people, culture, and community.

Target Market(s)

Patrons to our farm who are interested in weddings, events, or our flowers and vegetables.

Contact Information for Business Card

Name, address, cell email (Danielle Hoskins, 2716 Wrenfield Rd, Harlow Springs, CO 80617, cell 30.412.6638, email danielle@wrenfieldacres.com)

```html
<!DOCTYPE html>
<html lang="en">
<head>
<meta charset="utf-8">
<title>Wrenfield Acres — Business Card</title>
<link rel="stylesheet" href="https://fonts.googleapis.com/css2?family=Arimo:wght@400;700&display=swap">
<style>
  :root {
    --backdrop: #9b9b9b;
    --paper: #fafaf8;
    --sage: #667a65;
    --sage-text: #6f8a70;
    --bronze: #b8865a;
    --ink: #6b6b6b;
    --divider: #c9c9c4;
    --white: #ffffff;
  }
  * { box-sizing: border-box; margin: 0; padding: 0; }
  html, body {
    width: 1200px; height: 1050px; overflow: hidden;
    background: var(--backdrop);
    font-family: "Arimo", Arial, sans-serif;
  }
  .canvas { position: relative; width: 1200px; height: 1050px; }
  .card {
    position: absolute; left: 250px; width: 700px; height: 400px;
    border-radius: 4px;
    box-shadow: 0 14px 30px rgba(0,0,0,0.22);
  }
  .card--front { top: 100px; background: var(--paper); }
  .card--back { top: 550px; background: var(--sage); }

  .front-layout {
    display: flex; align-items: center; justify-content: center;
    height: 100%; gap: 34px;
  }
  .brand-name {
    color: var(--sage-text); font-weight: 400; font-size: 34px;
    letter-spacing: 1px; white-space: nowrap;
    display: flex; align-items: center; gap: 12px;
  }
  .brand-mark {
    width: 12px; height: 12px; border-radius: 50%; background: var(--bronze);
  }
  .divider { width: 1px; height: 150px; background: var(--divider); }
  .contact { color: var(--ink); font-size: 17px; line-height: 1.35; white-space: nowrap; }
  .contact-name {
    color: var(--sage-text); font-weight: 700; font-size: 24px; margin-bottom: 12px;
  }
  .contact-address { margin-bottom: 8px; }
  .contact-line { display: flex; align-items: center; gap: 10px; }
  .contact-line svg { width: 14px; height: 14px; flex: none; }

  .back-layout {
    display: flex; align-items: center; justify-content: center; height: 100%;
  }
  .back-name {
    color: var(--white); font-size: 54px; font-weight: 400; letter-spacing: 2px;
    display: flex; align-items: center; gap: 16px;
  }
  .back-name .brand-mark { width: 16px; height: 16px; }
</style>
</head>
<body>
<main class="canvas">
  <section class="card card--front">
    <div class="front-layout">
      <div class="brand-name"><span class="brand-mark"></span>Wrenfield Acres</div>
      <div class="divider"></div>
      <div class="contact">
        <p class="contact-name">Danielle Hoskins</p>
        <p class="contact-address">2716 Wrenfield Rd<br>Harlow Springs, CO 80617</p>
        <p class="contact-line">
          <svg viewBox="0 0 14 14" aria-hidden="true"><rect x="3" y="1" width="8" height="12" rx="1.5" fill="none" stroke="var(--bronze)" stroke-width="1.4"/></svg>
          30.412.6638
        </p>
        <p class="contact-line">
          <svg viewBox="0 0 14 14" aria-hidden="true"><rect x="1" y="3" width="12" height="8" fill="var(--bronze)"/><path d="M1 3 L7 8 L13 3" fill="none" stroke="var(--paper)" stroke-width="1"/></svg>
          danielle@wrenfieldacres.com
        </p>
      </div>
    </div>
  </section>

  <section class="card card--back">
    <div class="back-layout">
      <div class="back-name"><span class="brand-mark"></span>Wrenfield Acres</div>
    </div>
  </section>
</main>
</body>
</html>
```